Window posters

We want a design (Smiley tooth shaped/logo attached) that will be posted on a dental office windows (23"x23") with 11 different wording/colors for each tooth.
All 11 will have the office name on top (Maple lane grins) then:
1- Friendly dental place, Family dentistry.
2- Comprehensive, periodic, exams, cleanings, X-rays
3- Urgent care dentistry, dental emergencies, dental pain.
4- Extractions, immediate Guided implants, 3D scans.
5- Painless one day root canal treatment, conservative dentistry.
6- Cosmetic dentistry, bonding, digital smile makeover.
7- Clear aligners, True beam, Clarofit.
8- Same day crowns and bridges.
9- Partial and complete dentures, implants Overdenture.
10- All teeth fixed on Implants.
11- Sleep apnea appliances, sleep dentistry.

```html
<!DOCTYPE html>
<html lang="en">
<head>
<meta charset="utf-8">
<title>Maple lane grins – Window posters</title>
<link rel="stylesheet" href="https://fonts.googleapis.com/css2?family=Barlow+Condensed:wght@600;700&display=swap">
<style>
  :root {
    --page-bg: #ffffff;
    --card-bg: #e9ebee;
    --white: #ffffff;
    --yellow: #ffe14a;
    --magenta: #e4207f;
    --purple: #5b2a86;
    --name-ink: rgba(255,255,255,0.92);
  }
  * { box-sizing: border-box; margin: 0; padding: 0; }
  html, body { width: 1200px; height: 4000px; overflow: hidden; }
  body {
    position: relative;
    background: var(--page-bg);
    font-family: "Barlow Condensed", "Arial Narrow", sans-serif;
  }

  .poster {
    position: absolute;
    width: 400px;
    height: 400px;
    background: var(--card-bg);
    border: 8px solid var(--frame);
    padding: 36px;
  }
  .poster--feature {
    left: 320px;
    top: 110px;
    width: 560px;
    height: 560px;
    border-width: 12px;
    padding: 52px;
  }
  .poster__panel {
    width: 100%;
    height: 100%;
    border-radius: 28px;
    background: linear-gradient(160deg, var(--tone-light), var(--tone) 55%, var(--tone-dark));
    display: flex;
    flex-direction: column;
    align-items: center;
    justify-content: center;
    gap: 6px;
    padding: 24px;
    text-align: center;
    line-height: 1.05;
  }
  .poster__name {
    font-weight: 600;
    font-size: 22px;
    letter-spacing: 1px;
    text-transform: uppercase;
    color: var(--name-ink);
    margin-bottom: 8px;
  }
  .poster__line {
    font-weight: 700;
    font-size: 30px;
    color: var(--white);
  }
  .poster__line--small { font-size: 22px; }
  .poster--feature .poster__name { font-size: 30px; margin-bottom: 12px; }
  .poster--feature .poster__line { font-size: 42px; }

  .ink-yellow { color: var(--yellow); }
  .ink-magenta { color: var(--magenta); }
  .ink-purple { color: var(--purple); }
  .ink-white { color: var(--white); }

  .col-left { left: 120px; }
  .col-right { left: 680px; }
  .row-1 { top: 1000px; }
  .row-2 { top: 1600px; }
  .row-3 { top: 2200px; }
  .row-4 { top: 2800px; }
  .row-5 { top: 3400px; }

  .theme-teal    { --frame: #1c9d98; --tone: #2bbcb6; --tone-light: #5fd6cf; --tone-dark: #1c9490; }
  .theme-sky     { --frame: #3b6fb6; --tone: #3a9ae0; --tone-light: #6cc0f0; --tone-dark: #2a6fc0; }
  .theme-red     { --frame: #8a1c1f; --tone: #c8262c; --tone-light: #e45a4a; --tone-dark: #9a1c22; }
  .theme-green   { --frame: #3a8a3a; --tone: #6aa83a; --tone-light: #9ccc4a; --tone-dark: #4a8a2a; }
  .theme-plum    { --frame: #6a2a7a; --tone: #7b2c8c; --tone-light: #a04ab0; --tone-dark: #5a1a6a; }
  .theme-orange  { --frame: #e07a2a; --tone: #f3a21a; --tone-light: #fcc44a; --tone-dark: #e0820e; }
  .theme-pink    { --frame: #c0307a; --tone: #e85a9a; --tone-light: #f48ab8; --tone-dark: #cc3a80; }
  .theme-lagoon  { --frame: #1c8fa0; --tone: #1fa3b0; --tone-light: #4ac4cc; --tone-dark: #167f8c; }
  .theme-cobalt  { --frame: #2a4a8a; --tone: #1e6fc0; --tone-light: #4a9ae0; --tone-dark: #174f98; }
  .theme-rust    { --frame: #b84a2a; --tone: #e8662a; --tone-light: #f4944a; --tone-dark: #c84a1a; }
  .theme-mint    { --frame: #1e3a3a; --tone: #3fc4b8; --tone-light: #7ae0d4; --tone-dark: #249a90; }
</style>
</head>
<body>

<article class="poster poster--feature theme-teal">
  <div class="poster__panel">
    <p class="poster__name">Maple lane grins</p>
    <p class="poster__line ink-yellow">friendly dental place</p>
    <p class="poster__line ink-white">family dentistry</p>
  </div>
</article>

<article class="poster col-left row-1 theme-sky">
  <div class="poster__panel">
    <p class="poster__name">Maple lane grins</p>
    <p class="poster__line">comprehensive <span class="ink-yellow">exams</span></p>
    <p class="poster__line"><span class="ink-magenta">periodic</span> <span class="poster__line--small">exams cleanings</span></p>
    <p class="poster__line">x-rays</p>
  </div>
</article>

<article class="poster col-right row-1 theme-red">
  <div class="poster__panel">
    <p class="poster__name">Maple lane grins</p>
    <p class="poster__line">urgent care dentistry</p>
    <p class="poster__line ink-yellow">dental emergencies</p>
    <p class="poster__line poster__line--small">dental pain</p>
  </div>
</article>

<article class="poster col-left row-2 theme-green">
  <div class="poster__panel">
    <p class="poster__name">Maple lane grins</p>
    <p class="poster__line">extractions <span class="ink-yellow">3D scans</span></p>
    <p class="poster__line poster__line--small">immediate guided</p>
    <p class="poster__line">implants</p>
  </div>
</article>

<article class="poster col-right row-2 theme-plum">
  <div class="poster__panel">
    <p class="poster__name">Maple lane grins</p>
    <p class="poster__line">painless one day</p>
    <p class="poster__line">root canal treatment</p>
    <p class="poster__line poster__line--small">conservative dentistry</p>
  </div>
</article>

<article class="poster col-left row-3 theme-orange">
  <div class="poster__panel">
    <p class="poster__name">Maple lane grins</p>
    <p class="poster__line ink-purple">cosmetic dentistry</p>
    <p class="poster__line poster__line--small">digital smile makeover</p>
    <p class="poster__line ink-purple">bonding</p>
  </div>
</article>

<article class="poster col-right row-3 theme-pink">
  <div class="poster__panel">
    <p class="poster__name">Maple lane grins</p>
    <p class="poster__line">clear aligners</p>
    <p class="poster__line ink-yellow">True beam Clarofit</p>
  </div>
</article>

<article class="poster col-left row-4 theme-lagoon">
  <div class="poster__panel">
    <p class="poster__name">Maple lane grins</p>
    <p class="poster__line">Same day crowns</p>
    <p class="poster__line">and bridges</p>
  </div>
</article>

<article class="poster col-right row-4 theme-cobalt">
  <div class="poster__panel">
    <p class="poster__name">Maple lane grins</p>
    <p class="poster__line poster__line--small">partial and complete dentures</p>
    <p class="poster__line ink-magenta">implants overdenture</p>
  </div>
</article>

<article class="poster col-left row-5 theme-rust">
  <div class="poster__panel">
    <p class="poster__name">Maple lane grins</p>
    <p class="poster__line ink-purple">All teeth fixed</p>
    <p class="poster__line ink-purple">on Implants</p>
  </div>
</article>

<article class="poster col-right row-5 theme-mint">
  <div class="poster__panel">
    <p class="poster__name">Maple lane grins</p>
    <p class="poster__line">sleep apnea appliances</p>
    <p class="poster__line ink-yellow">sleep dentistry</p>
  </div>
</article>

</body>
</html>
```